Vex

I have the logo for the back already. Need the front to match.
Need a VEX logo which I can provide or you can download one - VEX Realty in canada... Back of the card will be my logo and name. Front will have the info...
I would like a black background. Match colors on front to the back..
Details on Card

Target Market(s)

Realestate clients.. Keep it classy like the logo

Contact Information for Business Card

Moren Tadwick office - 5817730264 cell - 5819063147 email - Moren@MorenTadwick.Com. website - MorenTadwick.Com Facebook - MTadwRealty Instagram - Moren_Qpl_Realtor Address - 418 - 23 St NE | K5P2M8

Colors
3176b5
33a6d7
85cae6

Requirements
Must have
• same color scheme as the logo
logo will be on the back
Black Background
Horizontal card
The one side of the card should be clean. like I stated, just my logo " Moren Tadwick " and nothing else

```html
<!DOCTYPE html>
<html lang="en">
<head>
<meta charset="utf-8">
<title>Moren Tadwick – Business Card Front</title>
<link rel="stylesheet" href="https://fonts.googleapis.com/css2?family=Cinzel:wght@600&family=Cormorant:wght@400;500&display=swap">
<style>
  :root {
    --page-bg: #ededed;
    --card-black: #1a1a1a;
    --brand-blue: #3176b5;
    --brand-mid: #33a6d7;
    --brand-light: #85cae6;
    --text-light: #e4e4e4;
  }
  * { box-sizing: border-box; margin: 0; padding: 0; }
  html, body {
    width: 1200px;
    height: 1200px;
    overflow: hidden;
    background: var(--page-bg);
  }
  .card {
    position: absolute;
    left: 60px;
    top: 291px;
    width: 1080px;
    height: 617px;
    background: var(--card-black);
    color: var(--text-light);
    font-family: "Cormorant", "Times New Roman", serif;
  }
  .card__name {
    position: absolute;
    left: 38px;
    top: 28px;
    font-family: "Cinzel", "Trajan Pro", serif;
    font-weight: 600;
    font-size: 80px;
    line-height: 1;
    letter-spacing: 1px;
    color: var(--brand-light);
    white-space: nowrap;
  }
  .card__mark {
    position: absolute;
    right: 40px;
    top: 210px;
    width: 270px;
    text-align: right;
    font-family: "Cinzel", "Trajan Pro", serif;
    font-weight: 600;
    font-size: 44px;
    line-height: 1.15;
    color: var(--brand-blue);
  }
  .contact {
    position: absolute;
    display: flex;
    align-items: center;
    gap: 14px;
    font-size: 29px;
    font-weight: 500;
    line-height: 1;
    font-variant-numeric: oldstyle-nums;
    white-space: nowrap;
  }
  .contact__icon {
    width: 26px;
    height: 26px;
    flex: none;
  }
  .contact__icon path,
  .contact__icon circle,
  .contact__icon rect,
  .contact__icon line {
    fill: none;
    stroke: var(--brand-blue);
    stroke-width: 1.6;
    stroke-linecap: round;
    stroke-linejoin: round;
  }
  .contact__icon .is-solid { fill: var(--brand-blue); stroke: none; }

  .contact--office  { left: 38px;  top: 380px; }
  .contact--cell    { left: 420px; top: 380px; }
  .contact--email   { left: 38px;  top: 436px; }
  .contact--web     { left: 420px; top: 436px; }
  .contact--social  { left: 38px;  top: 492px; }
  .contact--page    { left: 420px; top: 492px; }
  .contact--address { left: 180px; top: 548px; }
</style>
</head>
<body>
  <main class="card">
    <h1 class="card__name">MOREN TADWICK</h1>

    <div class="card__mark">Moren<br>Tadwick</div>

    <div class="contact contact--office">
      <svg class="contact__icon" viewBox="0 0 26 26" aria-hidden="true">
        <path d="M6 3 L10 3 L12 8 L9 10 Q11 15 16 17 L18 14 L23 16 L23 20 Q23 23 20 23 Q4 21 3 6 Q3 3 6 3 Z"/>
      </svg>
      <span>5817730264 (Office)</span>
    </div>

    <div class="contact contact--cell">
      <span>5819063147 (Cell)</span>
    </div>

    <div class="contact contact--email">
      <svg class="contact__icon" viewBox="0 0 26 26" aria-hidden="true">
        <rect x="2" y="6" width="22" height="15"/>
        <path d="M2 6 L13 15 L24 6"/>
        <path d="M2 21 L10 13 M24 21 L16 13"/>
      </svg>
      <span>moren@morentadwick.com</span>
    </div>

    <div class="contact contact--web">
      <svg class="contact__icon" viewBox="0 0 26 26" aria-hidden="true">
        <circle cx="13" cy="13" r="10.5"/>
        <path d="M13 2.5 Q7 13 13 23.5 M13 2.5 Q19 13 13 23.5"/>
        <line x1="2.5" y1="13" x2="23.5" y2="13"/>
        <line x1="4.5" y1="8" x2="21.5" y2="8"/>
        <line x1="4.5" y1="18" x2="21.5" y2="18"/>
      </svg>
      <span>morentadwick.com</span>
    </div>

    <div class="contact contact--social">
      <svg class="contact__icon" viewBox="0 0 26 26" aria-hidden="true">
        <rect x="3" y="3" width="20" height="20"/>
      </svg>
      <span>@Moren_Qpl_Realtor</span>
    </div>

    <div class="contact contact--page">
      <svg class="contact__icon" viewBox="0 0 26 26" aria-hidden="true">
        <rect class="is-solid" x="3" y="3" width="20" height="20"/>
      </svg>
      <span>MTadwRealty</span>
    </div>

    <div class="contact contact--address">
      <svg class="contact__icon" viewBox="0 0 26 26" aria-hidden="true">
        <path d="M2 13 L13 3 L24 13"/>
        <path d="M5 11 L5 23 L10 23 L10 16 L16 16 L16 23 L21 23 L21 11"/>
      </svg>
      <span>418 - 23 St NE | K5P2M8</span>
    </div>
  </main>
</body>
</html>
```